Corvane Facilities group

Corvane Facilities group is a facility services company provide security and cleaning services to corporate and retail sectors, we need high quality business card design for our company, the main company is (corvane facilities group) and the other companies is (corvane security group) and (corvane cleaning group), I have attached 3 logos the main logo is corvane facilities group and the other logos will be smaller.
Business card details:
Rory Tembeck
General Manager
Corvane Facilities Group
Mobil: 0427 615 392
Tell: 1300 574 906
Email: rory@corvanefacilities.com.au
Web: www.corvanefacilities.com.au
36/11-19 Pelham Street Bankstown NSW 2200
Services: Security, Cleaning, Facility Services
Slogan: Services, Protection, Integrity
Industry/Entity Type
Security

```html
<!DOCTYPE html>
<html lang="en">
<head>
<meta charset="utf-8">
<title>Corvane Facilities Group — Business Card</title>
<link rel="stylesheet" href="https://fonts.googleapis.com/css2?family=Source+Sans+3:wght@400;600;700&display=swap">
<style>
  :root {
    --navy: #0f3a5c;
    --navy-deep: #0a2c47;
    --navy-glow: #24557c;
    --red: #e31e2a;
    --white: #ffffff;
    --paper: #fafafa;
    --grey-text: #7a7a7a;
    --grey-line: #b9b9b9;
    --backdrop: #e9e6e1;
  }
  * { margin: 0; padding: 0; box-sizing: border-box; }
  html, body {
    width: 1200px; height: 1000px; overflow: hidden;
    background: var(--backdrop);
    font-family: "Source Sans 3", "Myriad Pro", Arial, sans-serif;
  }
  .canvas { position: relative; width: 1200px; height: 1000px; }

  /* Front card */
  .card-front {
    position: absolute; left: 60px; top: 63px; width: 695px; height: 410px;
    border-top-right-radius: 70px; overflow: hidden; background: var(--paper);
  }
  .card-front .split { position: absolute; inset: 0; }
  .service-list {
    position: absolute; left: 22px; top: 32px; width: 340px;
    transform-origin: 0 0; transform: translate(0, 0) rotate(90deg) translate(0, -30px);
    font-size: 13.5px; color: var(--grey-text); white-space: nowrap; letter-spacing: 0.2px;
  }
  .service-list .dot { color: var(--red); font-size: 12px; }
  .rule-vertical { position: absolute; left: 59px; top: 15px; width: 1px; height: 380px; background: var(--grey-line); }

  .sub-brands { position: absolute; left: 115px; top: 195px; display: flex; gap: 16px; }
  .sub-brand {
    width: 78px; font-size: 15px; font-weight: 700; line-height: 1.05;
    color: var(--navy); text-transform: lowercase;
  }

  .brand-main {
    position: absolute; left: 430px; top: 130px; width: 220px; text-align: center;
    color: var(--white); font-weight: 700; font-size: 30px; line-height: 1.05;
  }
  .slogan {
    position: absolute; left: 402px; top: 286px; width: 280px; text-align: center;
    color: var(--white); font-size: 15.5px;
  }
  .web-front {
    position: absolute; right: 17px; bottom: 20px;
    color: var(--red); font-size: 22px; letter-spacing: 0.3px;
  }

  /* Back card */
  .card-back {
    position: absolute; left: 408px; top: 520px; width: 702px; height: 412px;
    border-top-left-radius: 70px; overflow: hidden;
    background: radial-gradient(ellipse 55% 60% at 42% 38%, var(--navy-glow), var(--navy) 60%, var(--navy-deep));
    color: var(--white);
  }
  .web-vertical {
    position: absolute; left: 52px; top: 40px;
    transform-origin: 0 0; transform: rotate(90deg);
    color: var(--red); font-size: 22px; white-space: nowrap; letter-spacing: 0.3px;
  }
  .brand-corner {
    position: absolute; right: 40px; top: 45px; width: 120px; text-align: center;
    font-weight: 700; font-size: 22px; line-height: 1.05; color: var(--white);
  }
  .contact-name { position: absolute; left: 232px; top: 215px; font-size: 31px; font-weight: 700; }
  .contact-title { position: absolute; left: 232px; top: 250px; font-size: 15px; }
  .contact-email { position: absolute; left: 234px; top: 271px; font-size: 15px; color: var(--red); }
  .contact-phones { position: absolute; left: 236px; top: 333px; font-size: 19px; line-height: 24px; }
  .contact-phones .label { color: var(--red); margin-right: 4px; }
  .contact-divider { position: absolute; left: 395px; top: 337px; width: 1px; height: 42px; background: rgba(255,255,255,0.6); }
  .contact-address { position: absolute; left: 408px; top: 333px; font-size: 19px; line-height: 24px; }
</style>
</head>
<body>
<main class="canvas">

  <section class="card-front" aria-label="Business card front">
    <svg class="split" width="695" height="410" viewBox="0 0 695 410" aria-hidden="true">
      <defs>
        <radialGradient id="navyFront" cx="0.72" cy="0.45" r="0.6">
          <stop offset="0" stop-color="#24557c"/>
          <stop offset="0.6" stop-color="#0f3a5c"/>
          <stop offset="1" stop-color="#0a2c47"/>
        </radialGradient>
      </defs>
      <polygon points="405,0 695,0 695,410 293,410" fill="#e31e2a"/>
      <polygon points="427,0 695,0 695,410 315,410" fill="url(#navyFront)"/>
    </svg>
    <div class="rule-vertical"></div>
    <p class="service-list">
      <span class="dot">•</span> Security Services <span class="dot">•</span> Cleaning Services <span class="dot">•</span> Facility Services
    </p>
    <div class="sub-brands">
      <p class="sub-brand">corvane security group</p>
      <p class="sub-brand">corvane cleaning group</p>
    </div>
    <p class="brand-main">Corvane Facilities Group</p>
    <p class="slogan">Services. Protection. Integrity</p>
    <p class="web-front">www.corvanefacilities.com.au</p>
  </section>

  <section class="card-back" aria-label="Business card back">
    <p class="web-vertical">www.corvanefacilities.com.au</p>
    <p class="brand-corner">Corvane Facilities Group</p>
    <h1 class="contact-name">Rory Tembeck</h1>
    <p class="contact-title">General Manager</p>
    <p class="contact-email">rory@corvanefacilities.com.au</p>
    <p class="contact-phones">
      <span class="label">m.</span>0427 615 392<br>
      <span class="label">t.</span>1300 574 906
    </p>
    <div class="contact-divider"></div>
    <p class="contact-address">36/11-19 Pelham Street Bankstown<br>NSW 2200</p>
  </section>

</main>
</body>
</html>
```